Business Card for Wellness Clinic

We need a business card for our new logo. I want it to match the feel of the logo

Target Market(s)

Young professional families looking for holistic health care

Industry/Entity Type

Health And Wellness

Contact Information for Business Card

Our business Name: Brackenfield Health & wellness Centre, our phone #, email address...see attached old business card

Font styles to use
Sans Serif

Colors
33b8a4
cee9f5

Requirements
Must have
• my logo and business name
• Font is "Helvetica Neue LT Std 45 Light" and
• Only for "&" using font "Trajan pro bold"
• Use colors in the logo

```html
<!DOCTYPE html>
<html lang="en">
<head>
<meta charset="utf-8">
<title>Business Card – Brackenfield Health &amp; wellness Centre</title>
<link href="https://fonts.googleapis.com/css2?family=Lato:wght@300;400;700&display=swap" rel="stylesheet">
<style>
  :root {
    --teal: #2bb5a0;
    --teal-light: #7fd3c5;
    --ink: #1d2124;
    --paper: #ffffff;
    --backdrop: #e9e4de;
  }
  html, body {
    margin: 0;
    width: 1200px;
    height: 1200px;
    overflow: hidden;
    background: var(--backdrop);
    font-family: "Lato", Helvetica, Arial, sans-serif;
  }
  .card {
    position: absolute;
    left: 75px;
    top: 300px;
    width: 1050px;
    height: 600px;
    background: var(--paper);
    box-shadow: 0 12px 30px rgba(0,0,0,0.15);
    overflow: hidden;
  }
  .brand-band {
    position: absolute;
    left: 660px;
    top: 0;
    width: 250px;
    height: 600px;
    background: var(--teal);
  }
  .brand-name {
    position: absolute;
    left: 0;
    right: 0;
    top: 170px;
    text-align: center;
    color: var(--paper);
    font-weight: 400;
    font-size: 30px;
    letter-spacing: 0.5px;
  }
  .brand-dot {
    display: block;
    width: 18px;
    height: 18px;
    margin: 0 auto 14px;
    border-radius: 50%;
    background: var(--paper);
  }
  .band-pattern {
    position: absolute;
    left: 0;
    bottom: 0;
    width: 250px;
    height: 175px;
    background: linear-gradient(135deg, var(--teal-light), var(--teal));
  }
  .doctor-name {
    position: absolute;
    left: 70px;
    top: 104px;
    margin: 0;
    font-size: 46px;
    font-weight: 700;
    color: var(--ink);
    letter-spacing: 0.3px;
    white-space: nowrap;
  }
  .doctor-title {
    position: absolute;
    left: 72px;
    top: 172px;
    margin: 0;
    font-size: 30px;
    font-weight: 300;
    color: var(--ink);
  }
  .rule {
    position: absolute;
    background: var(--teal);
  }
  .rule-title { left: 70px; top: 232px; width: 560px; height: 7px; }
  .rule-contact-thin { left: 70px; top: 452px; width: 590px; height: 2px; }
  .rule-contact-thick { left: 70px; top: 560px; width: 590px; height: 6px; }
  .contact-list {
    position: absolute;
    left: 72px;
    top: 300px;
    margin: 0;
    padding: 0;
    list-style: none;
    font-size: 25px;
    font-weight: 400;
    color: var(--ink);
    line-height: 36px;
  }
  .contact-list b { font-weight: 700; display: inline-block; width: 22px; }
  .address {
    position: absolute;
    left: 72px;
    top: 470px;
    margin: 0;
    font-style: normal;
    font-size: 25px;
    line-height: 36px;
    color: var(--ink);
  }
</style>
</head>
<body>
  <div class="card">
    <h1 class="doctor-name">Dr. Clara Wensley, N.D</h1>
    <p class="doctor-title">Naturopathic Doctor</p>
    <div class="rule rule-title"></div>

    <ul class="contact-list">
      <li><b>t</b>: 613-555-0148</li>
      <li><b>f</b>: 888-555-0172</li>
      <li><b>e</b>: cwensley@brackenfieldnaturopathic.ca</li>
      <li><b>w</b>: www.brackenfieldnaturopathic.ca</li>
    </ul>
    <div class="rule rule-contact-thin"></div>
    <address class="address">418 Maple Grove Ave., Suite 210<br>Ottawa, ON K1R 5T7</address>
    <div class="rule rule-contact-thick"></div>

    <div class="brand-band">
      <div class="brand-name"><span class="brand-dot"></span>Brackenfield</div>
      <div class="band-pattern" role="img" aria-label="Decorative repeating leaf pattern"></div>
    </div>
  </div>
</body>
</html>
```